Webdesign für freie Trauungen
Zielgruppe
Webseite für Hochzeitspaare, Trauerende, Bestatter, Interessierte
Aufgabenstellung
Internetseite
Briefing:
Onepager
Internetseite soll wirken:
Modern
Schlank
Klar
Vertrauenserweckend
professionell
Home:
Reden für besondere Momente im Leben
Schrift an Flyer anpassen
REDEN.
ERZÄHLEN.
ERINNERN.
BERÜHREN.
Bild von mir,
Dazu, meine Reden sind:
freundlich
authentisch
ehrlich
einfühlsam
taktvoll
humorvoll
tiefsinnig
tröstend
nett
zugewandt
interessant
nach Euren Wünschen
mit Euren Inhalten
individuell
sehr persönlich
kreativ
wortgewandt
erfahren
Sprechen Sie mich an! ?
FREIE TRAUUNG:
EINFACH HIMMLISCH!
eine Liebesgeschichte erzählen
Sich ein Versprechen geben
JA zueinander sagen
Mit lieben Menschen feiern
wo, wann, wie - das entscheidet Ihr!
Segensfeier - Willkommensfeier:
im Leben willkommen heißen
Was bedeutet der Name des Kindes?
Was wollt Ihr Eurem Kind mitgeben?
Was wünscht Ihr Euch für Euer Kind?
TRAUERFEIER:
an schöne Momente erinnern
Einen Menschen mit Worten lebendig werden lassen
Mit einer persönlichen und bewegenden Ansprache
Mit all dem, was Sie sich wünschen!
REDEN ZU GEBURTSTAGEN:
mit Humor, Witz und Verstand gemeinsam zurück schauen
Und von Träumen und Sehnsüchten erzählen
Reden zum Jubiläum:
gemeinsam zurück schauen
Geleistetes würdigen
Veränderungen verständlich machen
Ausblicke wagen
Biographien:
festhalten, damit nichts von Ihrer Lebensgeschichte verloren geht
Sie erinnern sich und ich schreibe auf
Referenzen:
???? Wie am besten ???
Persönliches Vita:
Studium an der Hohen Akademie Talwerk:
- Publizistik
Germanistik
Volkswirtschaftslehre
Lateinamerikanistik
Abschluß: Magistra Artium
Freie Rednerin seit 1998
Telefonnummer 015923867214
Email: sabine.Meltorf@postwiese.de
Wirk..

```html
<!DOCTYPE html>
<html lang="de">
<head>
<meta charset="utf-8">
<title>Reden für besondere Momente – Angebote</title>
<link rel="stylesheet" href="https://fonts.googleapis.com/css2?family=Source+Sans+3:wght@400&family=Quicksand:wght@400;500&display=swap">
<style>
  :root {
    --page-bg: #f4f5f4;
    --card-bg: #ffffff;
    --accent: #5f8e8a;
    --text: #4a4a4a;
    --sketch: #e6eeee;
    --photo-warm-a: #c9a88b;
    --photo-warm-b: #6e5846;
    --photo-garden-a: #7d8a5c;
    --photo-garden-b: #3e4a32;
  }
  * { margin: 0; padding: 0; box-sizing: border-box; }
  html, body {
    width: 1200px; height: 1000px; overflow: hidden;
    background: var(--page-bg);
  }
  .offers { position: relative; width: 1200px; height: 1000px; }
  .offer-card {
    position: absolute; left: 134px; width: 929px; height: 312px;
    background: var(--card-bg);
    box-shadow: 0 6px 24px rgba(0,0,0,0.06);
  }
  .offer-card--blessing { top: 171px; }
  .offer-card--birthday { top: 529px; }
  .quote-badge {
    position: absolute; right: 40px; top: -13px;
    width: 32px; height: 32px; background: var(--accent);
    display: flex; align-items: center; justify-content: center;
  }
  .offer-photo {
    position: absolute; left: 41px; top: 37px; width: 356px; height: 237px;
  }
  .offer-photo--family { background: linear-gradient(120deg, var(--photo-warm-b), var(--photo-warm-a) 55%, #e9e2da); }
  .offer-photo--party { background: linear-gradient(160deg, var(--photo-garden-a), var(--photo-garden-b) 60%, #8a7a6a); }
  .offer-text { position: absolute; left: 463px; top: 56px; width: 300px; }
  .offer-card--birthday .offer-text { top: 56px; }
  .offer-title {
    font-family: "Source Sans 3", sans-serif; font-weight: 400;
    font-size: 21px; line-height: 27px; letter-spacing: 0.6px;
    color: var(--accent); text-transform: uppercase;
  }
  .offer-body {
    margin-top: 23px;
    font-family: "Quicksand", sans-serif; font-weight: 500;
    font-size: 16.5px; line-height: 21px; color: var(--text);
  }
  .offer-card--birthday .offer-body { margin-top: 28px; }
  .sketch { position: absolute; background: radial-gradient(ellipse at 60% 55%, var(--sketch), rgba(230,238,238,0) 70%); }
  .sketch--nursery { left: 680px; top: 159px; width: 229px; height: 143px; }
  .sketch--cake { left: 691px; top: 105px; width: 221px; height: 184px; }
</style>
</head>
<body>
<main class="offers">
  <article class="offer-card offer-card--blessing">
    <span class="quote-badge" aria-hidden="true">
      <svg width="18" height="14" viewBox="0 0 18 14"><path d="M1 1h7v6l-3 6H2l2-6H1z M10 1h7v6l-3 6h-3l2-6h-3z" fill="#fff"/></svg>
    </span>
    <div class="offer-photo offer-photo--family" role="img" aria-label="Foto: Eltern halten ihr lachendes Baby im Arm"></div>
    <div class="offer-text">
      <h2 class="offer-title">Segensfeier<br>Willkommensfeier</h2>
      <p class="offer-body">im Leben willkommen heißen<br>Was bedeutet der Name des Kindes?<br>Was wollt Ihr Eurem Kind mitgeben?<br>Was wünscht Ihr Euch für Euer Kind?</p>
    </div>
    <div class="sketch sketch--nursery" role="img" aria-label="Zarte Skizze: Teddybär, Babyflasche und Schnuller"></div>
  </article>

  <article class="offer-card offer-card--birthday">
    <span class="quote-badge" aria-hidden="true">
      <svg width="18" height="14" viewBox="0 0 18 14"><path d="M1 1h7v6l-3 6H2l2-6H1z M10 1h7v6l-3 6h-3l2-6h-3z" fill="#fff"/></svg>
    </span>
    <div class="offer-photo offer-photo--party" role="img" aria-label="Foto: Geburtstagsfeier im Garten mit Partyhüten"></div>
    <div class="offer-text">
      <h2 class="offer-title">Reden zu Geburtstagen</h2>
      <p class="offer-body">mit Humor, Witz und Verstand<br>gemeinsam zurück schauen<br>Und von Träumen und Sehnsüchten<br>erzählen</p>
    </div>
    <div class="sketch sketch--cake" role="img" aria-label="Zarte Skizze: Geburtstagstorte mit Kerzen und Luftschlangen"></div>
  </article>
</main>
</body>
</html>
```